Business card design needed

Hello, I Need a business card for a company that specialises in providing contract management services for civil construction projects - roads, bridges etc.
I do have a logo that i produced for PLOVER Civilworks however it probably needs a little work, the circles dont have defined edges, i was thinking the colours should reflect the dry interior of Australia progressing out to the colours of the ocean as you move towards the East.... that was my thinking anyway!
Target Market(s)
Professional people generally 30+ yrs old who need professional services to deliver contracts in a high risk environment
Industry/Entity Type
Construction
Contact Information for Business Card
PLOVER Civilworks
Darren Holbeck - Director and Principal Engineer
Registered Professional Engineer of Queensland
Phone 0438 615 272
Email darren@plovercivilworks.com.au
ABN 83 214 570 618
Logo Text
PLOVER Civilworks
Logo styles of interest
Pictorial/Combination Logo
Wordmark Logo
Lettermark Logo
Look and feel

```html
<!DOCTYPE html>
<html lang="en">
<head>
<meta charset="utf-8">
<title>PLOVER Civilworks – Business Card</title>
<link href="https://fonts.googleapis.com/css2?family=EB+Garamond:wght@400;500&display=swap" rel="stylesheet">
<style>
  :root {
    --backdrop: #2a2a2a;
    --ink: #1c1c1c;
    --red-earth: #ad3127;
    --desert-yellow: #f4d20e;
    --ocean-teal: #0f8479;
    --card-white: #fbfbfb;
    --card-shade: #e9e9e9;
  }
  * { box-sizing: border-box; margin: 0; padding: 0; }
  html, body {
    width: 1200px;
    height: 900px;
    overflow: hidden;
    background: var(--backdrop);
    font-family: "EB Garamond", Georgia, serif;
    color: var(--ink);
  }
  .canvas {
    position: relative;
    width: 1200px;
    height: 900px;
  }
  .card {
    position: absolute;
    width: 560px;
    height: 320px;
    box-shadow: 0 10px 30px rgba(0,0,0,0.55);
    overflow: hidden;
  }

  /* Front of card */
  .card-front {
    left: 110px;
    top: 130px;
    display: flex;
  }
  .band { height: 100%; }
  .band-red { width: 32%; background: var(--red-earth); }
  .band-yellow { width: 46%; background: var(--desert-yellow); }
  .band-teal { width: 22%; background: var(--ocean-teal); }
  .front-name {
    position: absolute;
    left: 0;
    right: 0;
    top: 50%;
    transform: translateY(-50%);
    text-align: center;
    font-size: 50px;
    font-weight: 500;
    color: var(--ink);
    letter-spacing: 0.5px;
  }

  /* Back of card */
  .card-back {
    left: 530px;
    top: 440px;
    background: linear-gradient(160deg, var(--card-white) 40%, var(--card-shade) 100%);
  }
  .person {
    position: absolute;
    left: 40px;
    top: 62px;
  }
  .person-name {
    font-size: 36px;
    font-weight: 400;
    letter-spacing: 0.5px;
    line-height: 1;
  }
  .person-role {
    margin-top: 8px;
    font-size: 15px;
    line-height: 1.2;
    color: var(--ocean-teal);
  }
  .contact {
    position: absolute;
    right: 36px;
    top: 80px;
    text-align: right;
    font-size: 14px;
    line-height: 1.3;
  }
  .contact-label {
    color: var(--ocean-teal);
    font-size: 13px;
    letter-spacing: 0.8px;
  }
  .contact-value { margin-bottom: 8px; }
  .brand {
    position: absolute;
    left: 40px;
    top: 196px;
    display: flex;
    align-items: center;
    gap: 10px;
  }
  .brand svg { display: block; }
  .brand-name {
    font-size: 20px;
    font-weight: 400;
    color: var(--ink);
  }
  .abn {
    position: absolute;
    left: 58px;
    bottom: 30px;
    font-size: 16px;
  }
  .abn-label { color: var(--ocean-teal); margin-right: 4px; }
</style>
</head>
<body>
  <main class="canvas">
    <section class="card card-front" aria-label="Business card front">
      <div class="band band-red"></div>
      <div class="band band-yellow"></div>
      <div class="band band-teal"></div>
      <h1 class="front-name">PLOVER Civilworks</h1>
    </section>

    <section class="card card-back" aria-label="Business card back">
      <div class="person">
        <h2 class="person-name">Darren Holbeck</h2>
        <p class="person-role">Director and Principal Engineer Registered<br>Professional Engineer of Queensland</p>
      </div>

      <div class="contact">
        <p class="contact-label">PHONE</p>
        <p class="contact-value">0438 615 272</p>
        <p class="contact-label">EMAIL</p>
        <p class="contact-value">darren@plovercivilworks.com.au</p>
      </div>

      <div class="brand">
        <svg width="34" height="34" viewBox="0 0 34 34" aria-hidden="true">
          <circle cx="17" cy="17" r="16" fill="var(--ocean-teal)"/>
        </svg>
        <span class="brand-name">PLOVER Civilworks</span>
      </div>

      <p class="abn"><span class="abn-label">ABN</span>83 214 570 618</p>
    </section>
  </main>
</body>
</html>
```